Maralby Information Posters for Student signage

Secondary school looking for some posters to display throughout the school with fresh designs using school colours and fitting with general feel of the school's graphic image. The final designs should be welcoming but clearly outline the required instructions. Sample designs that have been created by the school are attached with the relevant information that is required to appear on the signs. School would like a more dynamic design than the basic signs attached.
We are looking for:
- Large pop-up banner style size for the 2 posters called
"Ready for class" and "Morning Routine".
- Printable poster for the "Maralby Outdoor" sign.

Please incorporate a design feature of "the Maralby 1,2,3" into the posters and also use the Maralby Leaner values of Integrity, Compassion, Curiosity and Drive to help illustrate the content.

An option for design is to incorporate our school's first nations artwork into the design and i have also provided various extracts of design pieces that the school often uses in it's marketing materials.

Target Market(s)

Secondary School Students

Industry/Entity Type

Education

Colors
00AB8E
00BBA5
67D7C9
C6EFE9
E9F9F6
FFF300
FFF600
FEFA6F
FFFEC7
FFFEE8
FFC000
F8CF3A
FAE287
FDF2CF
FEFAEE

Requirements
Must have
• My project must have eyecatching graphics

```html
<!DOCTYPE html>
<html lang="en">
<head>
<meta charset="utf-8">
<title>Maralby Information Posters</title>
<link href="https://fonts.googleapis.com/css2?family=Teko:wght@500;600&family=Arimo:wght@700&display=swap" rel="stylesheet">
<style>
  :root {
    --green-deep: #1b3a1d;
    --green-mid: #234d26;
    --yellow: #fff300;
    --white: #ffffff;
    --page: #ffffff;
  }
  * { box-sizing: border-box; margin: 0; padding: 0; }
  html, body { width: 962px; height: 1200px; overflow: hidden; background: var(--page); }
  .canvas { position: relative; width: 962px; height: 1200px; }

  .poster {
    position: absolute; top: 147px; width: 380px; height: 906px; overflow: hidden;
    background: linear-gradient(180deg, var(--green-mid) 0%, var(--green-deep) 100%);
    font-family: "Teko", "Arial Narrow", sans-serif;
  }
  .poster--class { left: 76px; }
  .poster--hats { left: 506px; }

  .corner-art {
    position: absolute; top: -70px; right: -70px; width: 200px; height: 200px; border-radius: 50%;
    background: radial-gradient(circle, var(--yellow) 0 10%, #8fae6a 11% 40%, rgba(143,174,106,0.35) 41% 70%, transparent 71%);
  }

  .headline { position: absolute; left: 29px; line-height: 0.8; text-transform: uppercase; font-weight: 600; }
  .headline .line { display: block; white-space: nowrap; }
  .h-white { color: var(--white); }
  .h-yellow { color: var(--yellow); }

  .class-head { top: 30px; }
  .class-head .l1 { font-size: 50px; }
  .class-head .l2 { font-size: 86px; margin-top: 4px; }
  .class-head .l3 { font-size: 50px; margin-top: 4px; }

  .hats-head { top: 30px; }
  .hats-head .l1 { font-size: 50px; }
  .hats-head .l2 { font-size: 100px; margin-top: 4px; }
  .hats-head .l3 { font-size: 26px; margin-top: 8px; }

  .steps-title {
    position: absolute; left: 29px; top: 203px; font-size: 44px; line-height: 1; font-weight: 600;
    color: var(--yellow); text-transform: uppercase; display: flex; align-items: center; gap: 2px;
    white-space: nowrap;
  }
  .steps-pill {
    display: flex; gap: 5px; align-items: center; background: var(--yellow);
    border-radius: 14px; padding: 3px 6px; margin-top: -8px;
  }
  .steps-pill i {
    width: 18px; height: 18px; border-radius: 50%; background: var(--green-deep); color: var(--white);
    font-style: normal; font-family: "Arimo", Arial, sans-serif; font-size: 10px; line-height: 18px; text-align: center;
  }

  .brackets { position: absolute; left: 0; top: 0; width: 380px; height: 906px; }

  .step { position: absolute; left: 0; width: 380px; height: 120px; }
  .step .ring { position: absolute; left: 38px; top: 5px; width: 110px; height: 110px; }
  .step .icon { position: absolute; left: 63px; top: 30px; width: 60px; height: 60px; }
  .step .figure { border-radius: 50%; background: radial-gradient(circle, #e9efe6 0 30%, rgba(233,239,230,0.15) 60%, transparent 70%); }
  .step .badge { position: absolute; left: 146px; top: 33px; width: 52px; height: 54px; }
  .step .label {
    position: absolute; left: 214px; top: 0; height: 120px; width: 128px; display: flex; align-items: center;
    font-family: "Arimo", Arial, sans-serif; font-weight: 700; font-size: 20px; line-height: 1.3; color: var(--white);
  }
  .step-1 { top: 255px; }
  .step-2 { top: 415px; }
  .step-3 { top: 574px; }

  .footer-wave { position: absolute; left: 0; top: 740px; width: 380px; height: 166px; }
  .footer-text {
    position: absolute; left: 29px; top: 836px; font-family: "Arimo", Arial, sans-serif; font-weight: 700;
    font-size: 16px; line-height: 1.35; color: var(--green-deep);
  }
  .school-mark {
    position: absolute; left: 270px; top: 822px; display: flex; align-items: center; gap: 5px;
    font-family: "Arimo", Arial, sans-serif; font-weight: 700; font-size: 16px; color: var(--green-deep);
  }
  .school-mark b { width: 14px; height: 14px; border-radius: 50%; background: var(--green-deep); }
</style>
</head>
<body>
<main class="canvas">

  <section class="poster poster--class">
    <div class="corner-art" role="img" aria-label="First Nations dot artwork sunburst"></div>
    <h1 class="headline class-head">
      <span class="line l1 h-white">Are you</span>
      <span class="line l2 h-yellow">Ready</span>
      <span class="line l3"><span class="h-yellow">For</span> <span class="h-white">Class?</span></span>
    </h1>
    <div class="steps-title">The Maralby <span class="steps-pill"><i>1</i><i>2</i><i>3</i></span></div>

    <svg class="brackets" viewBox="0 0 380 906" aria-hidden="true">
      <g fill="none" stroke="#fff300" stroke-width="1.5">
        <path d="M322 221 H337 q12 0 12 12 V387 q0 12 -12 12 H34"/>
        <path d="M337 399 q12 0 12 12 V544 q0 12 -12 12 H34"/>
        <path d="M337 556 q12 0 12 12 V700 q0 12 -12 12 H34"/>
      </g>
      <g fill="#fff300"><circle cx="34" cy="399" r="4"/><circle cx="34" cy="556" r="4"/><circle cx="34" cy="712" r="4"/></g>
    </svg>

    <div class="step step-1">
      <svg class="ring" viewBox="0 0 110 110"><circle cx="55" cy="55" r="50" fill="none" stroke="#fff300" stroke-width="6" stroke-dasharray="0.1 9" stroke-linecap="round"/></svg>
      <svg class="icon" viewBox="0 0 60 60" aria-label="Laptop"><rect x="11" y="15" width="38" height="26" rx="2" fill="#fff"/><path d="M4 44 H56 l-3 5 H7 Z" fill="#fff"/></svg>
      <svg class="badge" viewBox="0 0 52 54"><path d="M0 0 H36 L52 27 L36 54 H0 Z" fill="#fff300"/><text x="22" y="42" text-anchor="middle" font-family="Arimo, Arial, sans-serif" font-weight="700" font-size="34" fill="#1b3a1d">1</text></svg>
      <p class="label">Laptop /<br>workbook</p>
    </div>

    <div class="step step-2">
      <svg class="ring" viewBox="0 0 110 110"><circle cx="55" cy="55" r="50" fill="none" stroke="#fff300" stroke-width="6" stroke-dasharray="0.1 9" stroke-linecap="round"/></svg>
      <svg class="icon" viewBox="0 0 60 60" aria-label="Phone pouch"><path d="M19 58 V12 a11 11 0 0 1 22 0 V58 Z" fill="#fff"/><circle cx="30" cy="11" r="3" fill="none" stroke="#1b3a1d" stroke-width="1.5"/><text x="30" y="50" text-anchor="middle" font-family="Arimo, Arial, sans-serif" font-size="5" fill="#1b3a1d">POUCHR</text></svg>
      <svg class="badge" viewBox="0 0 52 54"><path d="M0 0 H36 L52 27 L36 54 H0 Z" fill="#fff300"/><text x="22" y="42" text-anchor="middle" font-family="Arimo, Arial, sans-serif" font-weight="700" font-size="34" fill="#1b3a1d">2</text></svg>
      <p class="label">Phone in<br>Pouchr</p>
    </div>

    <div class="step step-3">
      <svg class="ring" viewBox="0 0 110 110"><circle cx="55" cy="55" r="50" fill="none" stroke="#fff300" stroke-width="6" stroke-dasharray="0.1 9" stroke-linecap="round"/></svg>
      <svg class="icon" viewBox="0 0 60 60" aria-label="Bucket hat"><path d="M17 38 Q18 22 30 22 Q42 22 43 38 Z" fill="#fff"/><path d="M5 44 Q30 34 55 44 Q30 50 5 44 Z" fill="#fff"/></svg>
      <svg class="badge" viewBox="0 0 52 54"><path d="M0 0 H36 L52 27 L36 54 H0 Z" fill="#fff300"/><text x="22" y="42" text-anchor="middle" font-family="Arimo, Arial, sans-serif" font-weight="700" font-size="34" fill="#1b3a1d">3</text></svg>
      <p class="label">Correct<br>uniform<br>(Including<br>hat)</p>
    </div>

    <svg class="footer-wave" viewBox="0 0 380 166" preserveAspectRatio="none" role="img" aria-label="First Nations dot artwork wave band">
      <path d="M0 30 C60 20 90 60 160 55 C240 48 300 10 380 5 V166 H0 Z" fill="#e9efe6" opacity="0.5"/>
      <path d="M0 45 C60 35 90 75 160 70 C240 63 300 25 380 20 V166 H0 Z" fill="#1b3a1d"/>
      <path d="M0 70 C60 70 100 100 170 95 C250 88 300 40 380 35 V166 H0 Z" fill="#fff300"/>
    </svg>
    <p class="footer-text">Curiosity and Drive<br>Maralby Learner Values</p>
    <div class="school-mark"><b></b>Maralby</div>
  </section>

  <section class="poster poster--hats">
    <div class="corner-art" role="img" aria-label="First Nations dot artwork sunburst"></div>
    <h1 class="headline hats-head">
      <span class="line l1 h-white">We wear</span>
      <span class="line l2 h-yellow">Hats</span>
      <span class="line l3 h-white">At Maralby when <span class="h-yellow">Outdoors...</span></span>
    </h1>
    <div class="steps-title">The Maralby <span class="steps-pill"><i>1</i><i>2</i><i>3</i></span></div>

    <svg class="brackets" viewBox="0 0 380 906" aria-hidden="true">
      <g fill="none" stroke="#fff300" stroke-width="1.5">
        <path d="M322 221 H337 q12 0 12 12 V387 q0 12 -12 12 H34"/>
        <path d="M337 399 q12 0 12 12 V544 q0 12 -12 12 H34"/>
        <path d="M337 556 q12 0 12 12 V700 q0 12 -12 12 H34"/>
      </g>
      <g fill="#fff300"><circle cx="34" cy="399" r="4"/><circle cx="34" cy="556" r="4"/><circle cx="34" cy="712" r="4"/></g>
    </svg>

    <div class="step step-1">
      <svg class="ring" viewBox="0 0 110 110"><circle cx="55" cy="55" r="50" fill="none" stroke="#fff300" stroke-width="6" stroke-dasharray="0.1 9" stroke-linecap="round"/></svg>
      <div class="icon figure" role="img" aria-label="Pictogram of a student walking in a hat"></div>
      <svg class="badge" viewBox="0 0 52 54"><path d="M0 0 H36 L52 27 L36 54 H0 Z" fill="#fff300"/><text x="22" y="42" text-anchor="middle" font-family="Arimo, Arial, sans-serif" font-weight="700" font-size="34" fill="#1b3a1d">1</text></svg>
      <p class="label">Walking</p>
    </div>

    <div class="step step-2">
      <svg class="ring" viewBox="0 0 110 110"><circle cx="55" cy="55" r="50" fill="none" stroke="#fff300" stroke-width="6" stroke-dasharray="0.1 9" stroke-linecap="round"/></svg>
      <div class="icon figure" role="img" aria-label="Pictogram of a student sitting in a hat"></div>
      <svg class="badge" viewBox="0 0 52 54"><path d="M0 0 H36 L52 27 L36 54 H0 Z" fill="#fff300"/><text x="22" y="42" text-anchor="middle" font-family="Arimo, Arial, sans-serif" font-weight="700" font-size="34" fill="#1b3a1d">2</text></svg>
      <p class="label">Sitting</p>
    </div>

    <div class="step step-3">
      <svg class="ring" viewBox="0 0 110 110"><circle cx="55" cy="55" r="50" fill="none" stroke="#fff300" stroke-width="6" stroke-dasharray="0.1 9" stroke-linecap="round"/></svg>
      <div class="icon figure" role="img" aria-label="Pictogram of a student playing ball in a hat"></div>
      <svg class="badge" viewBox="0 0 52 54"><path d="M0 0 H36 L52 27 L36 54 H0 Z" fill="#fff300"/><text x="22" y="42" text-anchor="middle" font-family="Arimo, Arial, sans-serif" font-weight="700" font-size="34" fill="#1b3a1d">3</text></svg>
      <p class="label">Playing</p>
    </div>

    <svg class="footer-wave" viewBox="0 0 380 166" preserveAspectRatio="none" role="img" aria-label="First Nations dot artwork wave band">
      <path d="M0 30 C60 20 90 60 160 55 C240 48 300 10 380 5 V166 H0 Z" fill="#e9efe6" opacity="0.5"/>
      <path d="M0 45 C60 35 90 75 160 70 C240 63 300 25 380 20 V166 H0 Z" fill="#1b3a1d"/>
      <path d="M0 70 C60 70 100 100 170 95 C250 88 300 40 380 35 V166 H0 Z" fill="#fff300"/>
    </svg>
    <p class="footer-text">Curiosity and Drive<br>Maralby Learner Values</p>
    <div class="school-mark"><b></b>Maralby</div>
  </section>

</main>
</body>
</html>
```